Iron Ridge Roofing Business Card

Need a business card with the logo that was designed here

Contact Information for Business Card

Name, Title, Phone, Email, Website, Company name

```html
<!DOCTYPE html>
<html lang="en">
<head>
<meta charset="utf-8">
<title>Iron Ridge Roofing – Business Card</title>
<link href="https://fonts.googleapis.com/css2?family=Open+Sans:wght@400;600;700&display=swap" rel="stylesheet">
<style>
  :root {
    --backdrop: #4a4a4a;
    --card-dark: #171717;
    --brand-blue: #1b78c2;
    --brand-blue-deep: #125e9e;
    --text-light: #f2f2f2;
  }
  * { box-sizing: border-box; margin: 0; padding: 0; }
  html, body { width: 1200px; height: 801px; overflow: hidden; }
  body {
    background: var(--backdrop);
    font-family: "Open Sans", Arial, sans-serif;
    display: flex;
    align-items: center;
    justify-content: center;
    gap: 40px;
  }
  .card {
    width: 525px;
    height: 300px;
    border-radius: 16px;
    position: relative;
    overflow: hidden;
  }
  .card--front {
    background: var(--card-dark);
    border: 3px solid var(--brand-blue);
    display: flex;
    align-items: center;
    padding: 0 30px;
  }
  .brand {
    flex: 1;
    display: flex;
    align-items: center;
    gap: 10px;
  }
  .brand__mark {
    width: 14px;
    height: 14px;
    background: var(--brand-blue);
    flex: none;
  }
  .brand__name {
    font-weight: 700;
    font-size: 25px;
    line-height: 1.15;
    color: var(--brand-blue);
  }
  .divider {
    width: 2px;
    height: 190px;
    background: var(--brand-blue);
    margin: 0 24px;
    flex: none;
  }
  .contact { flex: 1.2; color: var(--text-light); white-space: nowrap; }
  .contact__name {
    font-weight: 700;
    font-size: 20px;
    letter-spacing: 0.5px;
    color: var(--brand-blue);
    text-transform: uppercase;
  }
  .contact__title { font-size: 13px; margin-bottom: 16px; }
  .contact__address { font-size: 13px; line-height: 1.4; margin-bottom: 16px; }
  .contact__list { list-style: none; font-size: 13px; line-height: 1.6; }
  .contact__list li { display: flex; align-items: center; gap: 8px; }
  .contact__list svg { width: 12px; height: 12px; fill: var(--brand-blue); flex: none; }
  .card--back {
    background: var(--brand-blue);
    display: flex;
    align-items: center;
    justify-content: center;
  }
  .card--back .brand { flex: none; gap: 14px; }
  .card--back .brand__name { font-size: 40px; color: var(--brand-blue-deep); }
  .card--back .brand__mark { width: 20px; height: 20px; background: var(--brand-blue-deep); }
</style>
</head>
<body>
  <section class="card card--front">
    <div class="brand">
      <span class="brand__mark"></span>
      <span class="brand__name">Iron Ridge Roofing</span>
    </div>
    <div class="divider"></div>
    <div class="contact">
      <p class="contact__name">Dana Whitford</p>
      <p class="contact__title">Managing Director</p>
      <p class="contact__address">48 Larkspur Lane, Fairview<br>Oregon, 97024</p>
      <ul class="contact__list">
        <li><svg viewBox="0 0 24 24"><path d="M6.6 10.8a15.1 15.1 0 0 0 6.6 6.6l2.2-2.2a1 1 0 0 1 1-.25 11.4 11.4 0 0 0 3.6.6 1 1 0 0 1 1 1V20a1 1 0 0 1-1 1A17 17 0 0 1 3 4a1 1 0 0 1 1-1h3.5a1 1 0 0 1 1 1c0 1.25.2 2.45.6 3.6a1 1 0 0 1-.25 1z"/></svg>503 555 0187</li>
        <li><svg viewBox="0 0 24 24"><path d="M2 5h20v14H2zm2 2v.5l8 5 8-5V7l-8 5z"/></svg>hello@ironridgeroof.com</li>
        <li><svg viewBox="0 0 24 24"><path d="M12 2a10 10 0 1 0 0 20 10 10 0 0 0 0-20zm6.9 6h-3a15 15 0 0 0-1.3-4A8 8 0 0 1 18.9 8zM12 4c.8 1.2 1.5 2.6 1.9 4h-3.8c.4-1.4 1.1-2.8 1.9-4zM4.3 14a8 8 0 0 1 0-4h3.4a16 16 0 0 0 0 4zm.8 2h3a15 15 0 0 0 1.3 4A8 8 0 0 1 5.1 16zm3-8h-3a8 8 0 0 1 4.3-4 15 15 0 0 0-1.3 4zM12 20c-.8-1.2-1.5-2.6-1.9-4h3.8c-.4 1.4-1.1 2.8-1.9 4zm2.3-6H9.7a14 14 0 0 1 0-4h4.6a14 14 0 0 1 0 4zm.3 6a15 15 0 0 0 1.3-4h3a8 8 0 0 1-4.3 4zm1.7-6a16 16 0 0 0 0-4h3.4a8 8 0 0 1 0 4z"/></svg>www.ironridgeroof.com</li>
      </ul>
    </div>
  </section>

  <section class="card card--back">
    <div class="brand">
      <span class="brand__mark"></span>
      <span class="brand__name">Iron Ridge Roofing</span>
    </div>
  </section>
</body>
</html>
```